Transformative School Model Needs a Website. I am easy to work with.

Greetings:
I am creating a K-12 school that is a complete and total re-imagination of what education can be for children, families, communities, and the planet. While we will begin as a K-12 school, I really see it as a complete life cycle education (birth to death). I'm looking for a website to describe my new transformational educational model. I anticipate having 7-8 pages. I have all the copy ready.
I am the Founder. I am easy to work with, an effective communicator, and I’m very good at knowing what I want and providing specific and concrete detail, examples, and direction to make sure I use your time wisely.

```html
<!DOCTYPE html>
<html lang="en">
<head>
<meta charset="utf-8">
<title>Serene Accord Academy</title>
<link href="https://fonts.googleapis.com/css2?family=Montserrat:wght@500;600;700&family=Nunito:wght@400;600&family=Fira+Sans:wght@300&display=swap" rel="stylesheet">
<style>
:root{
  --blue:#0b55b6;
  --blue-deep:#0a4aa6;
  --title-blue:#0b4fae;
  --orange:#f1912d;
  --ink:#1b1b1b;
  --white:#ffffff;
  --sky:#9fbfe0;
  --line:#d9dde3;
}
*{box-sizing:border-box;margin:0;padding:0}
html,body{width:1200px;height:3210px;overflow:hidden}
body{position:relative;background:var(--white);font-family:"Nunito",sans-serif;color:var(--ink)}
.abs{position:absolute}

/* header */
.site-header{left:0;top:0;width:1200px;height:91px;background:var(--blue)}
.brand-badge{width:120px;height:120px;border-radius:50%;background:var(--white);box-shadow:0 3px 10px rgba(0,0,0,.25);display:flex;align-items:center;justify-content:center;text-align:center;font-family:"Montserrat",sans-serif;font-weight:600;font-size:12px;line-height:1.35;letter-spacing:1.5px;color:var(--title-blue)}
.brand-top{left:122px;top:12px;z-index:3}
.main-nav{left:432px;top:39px;display:flex;gap:0;font-family:"Montserrat",sans-serif;font-size:10.5px;font-weight:500;color:var(--white);letter-spacing:.2px}
.main-nav span{position:absolute;white-space:nowrap}
.donate{left:977px;top:32px;width:100px;height:29px;border-radius:15px;background:var(--orange);color:#1a1a1a;font-family:"Montserrat",sans-serif;font-weight:700;font-size:10px;letter-spacing:.5px;display:flex;align-items:center;justify-content:center}

/* hero */
.hero{left:0;top:91px;width:1200px;height:618px;background:linear-gradient(180deg,#6f7f91 0%,#a88c79 35%,#d59a63 55%,#5b3d2a 72%,#1a1410 100%)}
.hero-title{left:0;top:330px;width:1200px;text-align:center;font-family:"Montserrat",sans-serif;font-weight:600;font-size:55px;line-height:56px;color:var(--white)}

/* intro */
.section-title{font-family:"Montserrat",sans-serif;font-weight:700;font-size:25px;color:var(--title-blue);letter-spacing:.3px}
.body-copy{font-size:12.5px;line-height:21.7px;color:var(--ink)}
.intro-title{left:0;top:808px;width:1200px;text-align:center}
.intro-copy{left:300px;top:869px;width:600px;text-align:center}
.mandala-left{left:78px;top:894px;width:144px;height:144px;border-radius:50%;background:radial-gradient(circle,#eaf3fc 0%,#d5e7f8 60%,rgba(213,231,248,0) 72%)}
.mandala-right{left:1000px;top:766px;width:320px;height:320px;border-radius:50%;background:radial-gradient(circle,#eef5fc 0%,#d8e8f8 60%,rgba(216,232,248,0) 72%)}
.intro-rule{left:420px;top:1090px;width:780px;height:1px;background:var(--line)}

/* founder */
.founder-bg{left:0;top:1110px;width:1200px;height:735px;background:linear-gradient(180deg,#ffffff 0%,#e2ebf5 25%,#b9cfe6 60%,#7fa2ca 100%)}
.founder-photo{left:197px;top:1126px;width:362px;height:362px;border-radius:50%;border:4px solid var(--blue);background:linear-gradient(135deg,#4f7d6c 0%,#6f9a94 45%,#c9b8a5 75%,#f2eee8 100%)}
.founder-title{left:657px;top:1148px}
.founder-copy{left:657px;top:1206px;width:382px}

/* purpose */
.lower-bg{left:0;top:1844px;width:1200px;height:698px;background:linear-gradient(180deg,#f1912d 0%,#f3ad6e 14%,#f7cfa7 35%,#f5dccb 60%,#f3d2c6 80%,#d6e7ea 100%)}
.purpose{left:111px;top:1614px;width:959px;height:335px;background:linear-gradient(90deg,#8a7156 0%,#b78a55 25%,#7f7560 55%,#4b4a3e 80%,#3b3a30 100%)}
.purpose-title{left:0;top:1719px;width:1200px;text-align:center;font-family:"Montserrat",sans-serif;font-weight:700;font-size:25px;color:var(--white);letter-spacing:.5px}
.purpose-copy{left:300px;top:1768px;width:600px;text-align:center;font-family:"Fira Sans",sans-serif;font-weight:300;font-size:19.5px;line-height:27.5px;color:var(--white)}
.lotus{border-radius:50%;background:radial-gradient(circle,#f06aa0 0%,#f5a9c8 45%,#f8e4ee 75%,rgba(248,228,238,0) 100%)}
.lotus-right{left:1132px;top:1790px;width:80px;height:80px}

/* equity */
.equity-title{left:194px;top:2085px;font-family:"Montserrat",sans-serif;font-weight:700;font-size:26px;line-height:35px;color:#111;letter-spacing:.3px}
.equity-copy{left:194px;top:2192px;width:390px}
.equity-photo{left:679px;top:2024px;width:344px;height:449px;border-radius:170px 170px 60px 170px;background:linear-gradient(160deg,#d8d3c8 0%,#cfa98a 40%,#e7e2dc 75%,#f5f4f2 100%)}

/* testimonials */
.testimonials{left:0;top:2542px;width:1200px;height:417px;background:var(--orange)}
.testimonials-title{left:0;top:2611px;width:1200px;text-align:center;font-family:"Montserrat",sans-serif;font-weight:700;font-size:25px;color:var(--white);letter-spacing:.5px}
.card{top:2686px;width:277px;height:198px;border-radius:20px;background:var(--white);box-shadow:0 2px 6px rgba(0,0,0,.08)}
.avatar{position:absolute;left:31px;top:27px;width:50px;height:50px;border-radius:50%;background:linear-gradient(135deg,#c9a58a,#8d6a55)}
.card-name{position:absolute;left:87px;top:43px;font-family:"Nunito",sans-serif;font-weight:600;font-size:13.5px;color:#111}
.card-text{position:absolute;left:31px;top:100px;width:220px;font-size:12.5px;line-height:17.5px;color:#111}
.arrow{top:2760px;width:24px;height:24px}

/* footer */
.site-footer{left:0;top:2959px;width:1200px;height:251px;background:linear-gradient(180deg,#0b55b6 0%,#2a77d0 55%,#5a9ae0 100%)}
.brand-bottom{left:557px;top:2922px;z-index:3}
.lotus-left{left:66px;top:2905px;width:150px;height:150px;z-index:3}
.footer-nav{font-family:"Montserrat",sans-serif;font-size:10.5px;font-weight:500;color:var(--white)}
.footer-nav span{position:absolute;white-space:nowrap}
.contact{top:3115px;font-family:"Montserrat",sans-serif;font-size:10.5px;color:var(--white)}
.contact-divider{left:552px;top:3107px;width:1px;height:26px;background:var(--white)}
</style>
</head>
<body>

<header class="abs site-header"></header>
<div class="abs brand-badge brand-top">SERENE<br>ACCORD</div>
<nav class="abs main-nav">
  <span style="left:0">SCHOOL FOUNDATIONS</span>
  <span style="left:137px">CURRICULUM</span>
  <span style="left:224px">PEDAGOGY</span>
  <span style="left:301px">OUTCOMES</span>
  <span style="left:373px">OPENING</span>
  <span style="left:441px">TESTIMONIALS</span>
</nav>
<div class="abs donate">DONATE</div>

<section class="abs hero" role="img" aria-label="Family silhouetted on coastal rocks at sunset"></section>
<h1 class="abs hero-title">Lorem ipsum dolor sit<br>amet consectetur. Purus</h1>

<div class="abs mandala-left" role="img" aria-label="Faint geometric ornament"></div>
<div class="abs mandala-right" role="img" aria-label="Faint geometric ornament"></div>
<h2 class="abs section-title intro-title">INTRODUCTION</h2>
<p class="abs body-copy intro-copy">The Planet is calling upon our consciousness to shift. While there is much to celebrate in the beauty and love that resides on Planet Earth, there is some tending to do. The water, soil, and air are sick. Animals—including men and women—find themselves living in inhospitable and sometimes violent environments. So, tending we must. Education and Evolution are inextricably linked. Wisdom always serves to guide us (with courage) forward into unknown and new—yet promising—territory. Our strength will persevere and grow. With joy and grace, we'll do the work of restoring and rebuilding the planet such that life sustains and thrives. Serene Accord Academy is starting a school to do just that.</p>
<div class="abs intro-rule"></div>

<div class="abs founder-bg"></div>
<div class="abs founder-photo" role="img" aria-label="Founder raising her arms by a lake"></div>
<h2 class="abs section-title founder-title">FOUNDER</h2>
<p class="abs body-copy founder-copy">The Planet is calling upon our consciousness to shift. While there is much to celebrate in the beauty and love that resides on Planet Earth, there is some tending to do. The water, soil, and air are sick. Animals—including men and women—find themselves living in inhospitable and sometimes violent environments. So, tending we must. Education and Evolution are inextricably linked. Wisdom always serves to guide us (with courage) forward into unknown and new—yet promising—territory. Our strength will persevere and grow. With joy and grace, we'll do the work of restoring and rebuilding the planet such that life sustains and thrives. Serene Accord Academy is starting a school to do just that.</p>

<div class="abs lower-bg"></div>
<section class="abs purpose" role="img" aria-label="Woman meditating with open arms by a lake at sunrise"></section>
<h2 class="abs purpose-title">PURPOSE</h2>
<p class="abs purpose-copy">We design for people to flourish, participate in public life, and live in harmony with the planet through aligning their souls, minds, and bodies to their hearts and collective imagination</p>
<div class="abs lotus lotus-right" role="img" aria-label="Pink lotus flower"></div>

<h2 class="abs equity-title">STATEMENT OF<br>ONENESS IN EQUITY</h2>
<p class="abs body-copy equity-copy">The Planet is calling upon our consciousness to shift. While there is much to celebrate in the beauty and love that resides on Planet Earth, there is some tending to do. The water, soil, and air are sick. Animals—including men and women—find themselves living in inhospitable and sometimes violent environments. So, tending we must. Education and Evolution are inextricably linked. Wisdom always serves to guide us (with courage) forward into unknown and new—yet promising—territory. Our strength will persevere and grow. With joy and grace, we'll do the work of restoring and rebuilding the planet such that life sustains and thrives. Serene Accord Academy is starting a school to do just that.</p>
<div class="abs equity-photo" role="img" aria-label="Parent and two children learning together at a laptop"></div>

<section class="abs testimonials"></section>
<h2 class="abs testimonials-title">TESTIMONIAL</h2>
<svg class="abs arrow" style="left:129px" viewBox="0 0 24 24" aria-hidden="true"><path d="M20 12H4M11 5l-7 7 7 7" fill="none" stroke="#fff" stroke-width="1.6"/></svg>
<svg class="abs arrow" style="left:1060px" viewBox="0 0 24 24" aria-hidden="true"><path d="M4 12h16M13 5l7 7-7 7" fill="none" stroke="#fff" stroke-width="1.6"/></svg>
<article class="abs card" style="left:176px">
  <div class="avatar" role="img" aria-label="Reviewer portrait"></div>
  <div class="card-name">Jhon Doe</div>
  <p class="card-text">Lorem ipsum dolor sit amet consectetur. Odio ultricies diam arcu interdum laoreet purus est.</p>
</article>
<article class="abs card" style="left:472px">
  <div class="avatar" role="img" aria-label="Reviewer portrait"></div>
  <div class="card-name">Jhon Doe</div>
  <p class="card-text">Lorem ipsum dolor sit amet consectetur. Odio ultricies diam arcu interdum laoreet purus est.</p>
</article>
<article class="abs card" style="left:768px">
  <div class="avatar" role="img" aria-label="Reviewer portrait"></div>
  <div class="card-name">Jhon Doe</div>
  <p class="card-text">Lorem ipsum dolor sit amet consectetur. Odio ultricies diam arcu interdum laoreet purus est.</p>
</article>

<footer class="abs site-footer"></footer>
<div class="abs lotus lotus-left" role="img" aria-label="Pink lotus flower"></div>
<div class="abs brand-badge brand-bottom">SERENE<br>ACCORD</div>
<nav class="abs footer-nav" style="left:0;top:3085px;width:1200px">
  <span style="left:322px">SCHOOL FOUNDATIONS</span>
  <span style="left:467px">CURRICULUM</span>
  <span style="left:560px;top:-3px">PEDAGOGY</span>
  <span style="left:643px;top:-3px">OUTCOMES</span>
  <span style="left:731px;top:-5px">OPENING</span>
  <span style="left:804px;top:-5px">TESTIMONIALS</span>
</nav>
<div class="abs contact" style="left:473px">555-014-2290</div>
<div class="abs contact-divider"></div>
<div class="abs contact" style="left:561px">hello@sereneaccordacademy.org</div>

</body>
</html>
```